Now Leasing Banner

Looking for a banner that says the following information approx 4' x 30'

Now Leasing Maplewood Terrace 925-318-6054

Target Market(s)

Drive by traffic

Industry/Entity Type

Residential property management

Requirements
Must have
• Clear and readable from a distance

```html
<!DOCTYPE html>
<html lang="en">
<head>
<meta charset="utf-8">
<title>Now Leasing Banner</title>
<link href="https://fonts.googleapis.com/css2?family=Bebas+Neue&family=Caveat+Brush&family=Exo+2:wght@700&display=swap" rel="stylesheet">
<style>
  :root {
    --page: #ffffff;
    --banner-white: #ffffff;
    --leaf-green: #93ae58;
    --navy: #1f2d6b;
    --red: #e93a35;
    --photo-sky: #6f9cc9;
    --photo-wall: #c9b48e;
    --skin: #d98f6c;
    --key-brass: #c9973f;
  }
  html, body {
    margin: 0;
    padding: 0;
    width: 1200px;
    height: 1108px;
    overflow: hidden;
    background: var(--page);
  }
  .banner {
    position: absolute;
    left: 40px;
    top: 472px;
    width: 1120px;
    height: 163px;
    background: var(--banner-white);
    box-shadow: 0 2px 6px rgba(0,0,0,0.18);
    overflow: hidden;
  }
  .banner-shapes {
    position: absolute;
    inset: 0;
  }
  .property-name {
    position: absolute;
    left: 160px;
    top: 20px;
    width: 360px;
    text-align: center;
    font-family: "Caveat Brush", cursive;
    font-size: 44px;
    line-height: 1;
    color: var(--navy);
    white-space: nowrap;
  }
  .property-phone {
    position: absolute;
    left: 160px;
    top: 90px;
    width: 350px;
    text-align: center;
    font-family: "Exo 2", sans-serif;
    font-weight: 700;
    font-size: 46px;
    line-height: 1;
    color: var(--navy);
    letter-spacing: 0.5px;
    white-space: nowrap;
  }
  .headline {
    position: absolute;
    left: 576px;
    top: 38px;
    margin: 0;
    font-family: "Bebas Neue", sans-serif;
    font-weight: 400;
    font-size: 102px;
    line-height: 1;
    color: var(--red);
    text-shadow: 4px 3px 0 var(--navy);
    white-space: nowrap;
    letter-spacing: 1px;
  }
</style>
</head>
<body>
  <section class="banner" aria-label="Now leasing banner">
    <svg class="banner-shapes" width="1120" height="163" viewBox="0 0 1120 163">
      <defs>
        <linearGradient id="photo-fade" x1="0" y1="0" x2="1" y2="0">
          <stop offset="0" stop-color="var(--photo-wall)"/>
          <stop offset="0.6" stop-color="var(--photo-wall)"/>
          <stop offset="1" stop-color="var(--leaf-green)"/>
        </linearGradient>
        <linearGradient id="photo-sky" x1="0" y1="0" x2="1" y2="0">
          <stop offset="0" stop-color="var(--photo-sky)"/>
          <stop offset="0.7" stop-color="var(--photo-sky)" stop-opacity="0.6"/>
          <stop offset="1" stop-color="var(--photo-sky)" stop-opacity="0"/>
        </linearGradient>
        <linearGradient id="hand-tone" x1="0" y1="0" x2="0" y2="1">
          <stop offset="0" stop-color="var(--skin)"/>
          <stop offset="1" stop-color="var(--key-brass)"/>
        </linearGradient>
      </defs>
      <polygon class="green-panel" points="0,0 477,0 582,163 0,163" fill="var(--leaf-green)"/>
      <g role="img" aria-label="Photo of the apartment building exterior">
        <rect class="building-photo" x="0" y="0" width="165" height="163" fill="url(#photo-fade)"/>
        <rect x="0" y="0" width="165" height="40" fill="url(#photo-sky)"/>
      </g>
      <rect class="hand-keys-photo" role="img" aria-label="Photo of a hand holding house keys"
            x="1034" y="30" width="86" height="114" rx="14" fill="url(#hand-tone)"/>
    </svg>
    <div class="property-name">Maplewood Terrace</div>
    <div class="property-phone">925-318-6054</div>
    <h1 class="headline">NOW LEASING</h1>
  </section>
</body>
</html>
```